Design for online reviews widget

Attached is a wireframe of a widget we need designing to display reviews on websites from multiple sources. We need this provided at 3 different sizes including full screen, contained (like the wireframe) and mobile.
You have completely free rein on the styling.
The only elements that should remain untouched are the blue stars (https://www.filquarry.net/s/8vtmwp2291zq4h/kv%20stars.ai?dl=0) and powered by logo at the bottom.
Ignore the menu at the top of the wireframe, this is just from the website the widget will be placed on.
Businesses

```html
<!DOCTYPE html>
<html lang="en">
<head>
<meta charset="utf-8">
<title>Review Widget – Three Sizes</title>
<link rel="stylesheet" href="https://fonts.googleapis.com/css2?family=Poppins:wght@400;500;600&display=swap">
<style>
:root{
  --stage:#777777;
  --panel:#ffffff;
  --ink:#1d1d1f;
  --muted:#3a3a3a;
  --accent:#33b4e6;
  --accent-dark:#1a84c4;
  --button:#3cbeef;
  --gold:#e8b931;
  --green:#3cb54a;
  --purple:#6a4be0;
  --ring:#0f5ea8;
  --line:#eeeeee;
}
*{box-sizing:border-box;margin:0;padding:0}
html,body{width:851px;height:1200px;overflow:hidden;background:var(--stage)}
body{position:relative;font-family:"Poppins",sans-serif;color:var(--ink)}

.screen-label{position:absolute;color:#fff;font-weight:500;letter-spacing:.5px;text-align:center}
.screen-label--full{left:25px;width:577px;top:12px;font-size:23px}
.screen-label--mobile{left:623px;width:215px;top:12px;font-size:23px}
.screen-label--contained{left:25px;width:577px;top:612px;font-size:15px;font-weight:400}

.widget{position:absolute;background:var(--panel);display:flex;flex-direction:column}
.widget--full{left:25px;top:52px;width:577px;height:551px}
.widget--contained{left:25px;top:637px;width:577px;height:551px}
.widget--mobile{left:623px;top:52px;width:215px;height:1136px}

.score{display:flex;flex-direction:column;align-items:center;justify-content:center;flex:none}
.score__stars{display:flex;gap:7px}
.score__stars svg{width:24px;height:24px}
.score__caption{font-size:6.3px;font-weight:500;margin-top:4px}
.widget--full .score,.widget--contained .score{height:58px;padding-top:2px}
.widget--mobile .score{height:82px;padding-top:6px}
.widget--mobile .score__stars{gap:8px}
.widget--mobile .score__stars svg{width:23px;height:23px}
.widget--mobile .score__caption{font-size:9px;margin-top:6px}

.review{background:#fff;box-shadow:0 0 3px rgba(0,0,0,.12);overflow:hidden;display:flex;flex:none}
.review__source{display:flex;flex-direction:column;align-items:center;justify-content:center;flex:none;gap:8px}
.brand{display:flex;align-items:center;gap:4px;font-weight:500;color:var(--ink);white-space:nowrap}
.brand__mark{width:8px;height:8px;border-radius:50%;background:var(--accent)}
.score-ring{width:38px;height:38px;border-radius:50%;border:4px solid var(--ring);display:flex;align-items:center;justify-content:center;box-shadow:inset 0 0 0 2px #fff,inset 0 0 0 14px var(--ring);color:#fff;font-size:6.5px;font-weight:500}
.rating{color:var(--gold);letter-spacing:1px;white-space:nowrap;line-height:1}

.review__title{font-weight:500;line-height:1.3}
.review__text{color:var(--muted);font-weight:400}
.hl{color:var(--accent);font-weight:500}
.metrics{display:flex;flex-wrap:wrap;align-items:center;color:var(--ink)}
.metrics span{padding:0 5px;border-left:1.5px solid var(--accent)}
.metrics span:first-child{padding-left:0;border-left:none}
.meta{display:flex;align-items:center;gap:8px;font-weight:500}
.meta svg{width:9px;height:9px;flex:none}
.meta-row{display:flex;justify-content:space-between;align-items:center}
.meta--plain{font-weight:400}

/* full */
.widget--full .reviews{display:flex;flex-direction:column}
.widget--full .review{width:100%}
.widget--full .review__source{width:144px}
.widget--full .review__body{width:420px;padding-top:11px}
.widget--full .review__title{font-size:11px}
.widget--full .review__text{font-size:6.2px;line-height:10.8px;margin-top:1px}
.widget--full .metrics{font-size:7.6px;margin-top:9px}
.widget--full .meta{font-size:7.8px;margin-top:10px}

/* contained */
.widget--contained .reviews{display:flex;flex-direction:column;align-items:center}
.widget--contained .review{width:455px;border-radius:3px}
.widget--contained .review__source{width:120px}
.widget--contained .review__body{width:325px;padding-top:11px}
.widget--contained .review__title{font-size:11px}
.widget--contained .review__text{font-size:6.2px;line-height:8.4px;margin-top:1px}
.widget--contained .metrics{font-size:7.6px;margin-top:6px}
.widget--contained .meta{font-size:7.8px;margin-top:9px}

.brand--lg{font-size:15px}
.rating--lg{font-size:16px}

/* mobile */
.widget--mobile .reviews{display:flex;flex-direction:column;align-items:center}
.widget--mobile .review{width:204px;flex-direction:column;border-radius:3px;padding:0 14px}
.widget--mobile .review__source{flex-direction:row;gap:14px;justify-content:center}
.widget--mobile .review__title{font-size:8.3px;line-height:12.5px}
.widget--mobile .review__text{font-size:6.1px;line-height:9.1px;margin-top:5px}
.widget--mobile .metrics{font-size:7px;margin-top:10px;row-gap:3px}
.widget--mobile .meta{font-size:7px;margin-top:12px}
.widget--mobile .meta--big{font-size:9px;margin-top:11px}
.widget--mobile .meta--big svg{width:11px;height:11px}
.brand--md{font-size:13px}
.rating--md{font-size:13px}
.score-ring--sm{width:32px;height:32px;font-size:5px;border-width:3px;box-shadow:inset 0 0 0 2px #fff,inset 0 0 0 12px var(--ring)}

.footer{position:relative;flex:1}
.load-more{position:absolute;background:var(--button);color:#fff;border:none;font-family:inherit;font-weight:500;border-radius:2px;display:flex;align-items:center;justify-content:center}
.powered{position:absolute;display:flex;flex-direction:column;align-items:flex-end}
.powered__label{font-weight:400}
.powered__name{display:flex;align-items:center;gap:4px;font-weight:600;color:var(--ink)}
.powered__name i{display:block;border-radius:50%;background:var(--accent)}
.widget--full .load-more,.widget--contained .load-more{width:83px;height:25px;font-size:7.5px;left:247px}
.widget--full .load-more{top:14px}
.widget--full .powered{right:20px;top:8px}
.widget--contained .load-more{top:11px}
.widget--contained .powered{right:61px;top:7px}
.widget--full .powered__label,.widget--contained .powered__label{font-size:7px}
.widget--full .powered__name,.widget--contained .powered__name{font-size:11px;margin-top:2px}
.widget--full .powered__name i,.widget--contained .powered__name i{width:20px;height:20px}
.widget--mobile .load-more{width:91px;height:27px;font-size:8.5px;left:62px;top:15px}
.widget--mobile .powered{right:5px;top:58px}
.widget--mobile .powered__label{font-size:5px}
.widget--mobile .powered__name{font-size:8.5px}
.widget--mobile .powered__name i{width:14px;height:14px}
</style>
</head>
<body>
<svg width="0" height="0" style="position:absolute" aria-hidden="true">
  <defs>
    <symbol id="star-badge" viewBox="0 0 40 40">
      <circle cx="20" cy="20" r="19.5" fill="#2aa9e3"/>
      <circle cx="20" cy="20" r="15" fill="none" stroke="#fff" stroke-width="1.6"/>
      <polygon points="20,9 22.6,16.4 30.5,16.6 24.2,21.4 26.5,29 20,24.6 13.5,29 15.8,21.4 9.5,16.6 17.4,16.4" fill="#fff"/>
    </symbol>
    <symbol id="icon-time" viewBox="0 0 10 12">
      <path d="M1.5 1h7M1.5 11h7M2.5 1c0 3 2.5 3.8 2.5 5S2.5 8 2.5 11M7.5 1c0 3-2.5 3.8-2.5 5s2.5 2 2.5 5" fill="none" stroke="#6a4be0" stroke-width="1.5" stroke-linecap="round"/>
    </symbol>
    <symbol id="icon-verified" viewBox="0 0 12 12">
      <rect x="0.5" y="0.5" width="11" height="11" rx="2" fill="#3cb54a"/>
      <polyline points="3,6.2 5.2,8.3 9.2,3.8" fill="none" stroke="#fff" stroke-width="1.6"/>
    </symbol>
    <symbol id="icon-pin" viewBox="0 0 12 12">
      <rect x="0.5" y="0.5" width="11" height="11" rx="2" fill="#3cb54a"/>
      <path d="M6 2.5a2.6 2.6 0 0 0-2.6 2.6C3.4 7 6 9.6 6 9.6S8.6 7 8.6 5.1A2.6 2.6 0 0 0 6 2.5z" fill="#fff"/>
      <circle cx="6" cy="5.1" r="1" fill="#3cb54a"/>
    </symbol>
  </defs>
</svg>

<h2 class="screen-label screen-label--full">FULL SCREEN</h2>
<h2 class="screen-label screen-label--mobile">MOBILE SCREEN</h2>
<h2 class="screen-label screen-label--contained">CONTAINED SCREEN</h2>

<!-- Full screen -->
<section class="widget widget--full">
  <header class="score">
    <div class="score__stars"><svg><use href="#star-badge"/></svg><svg><use href="#star-badge"/></svg><svg><use href="#star-badge"/></svg><svg><use href="#star-badge"/></svg><svg><use href="#star-badge"/></svg></div>
    <p class="score__caption">Combined Review Score 4.3 out of 5</p>
  </header>
  <div class="reviews">
    <article class="review" style="height:115px">
      <div class="review__source"><span class="brand brand--lg"><i class="brand__mark"></i>TradeTally</span><div class="score-ring">9.77</div></div>
      <div class="review__body">
        <h3 class="review__title">Front door with windows each side and side window</h3>
        <p class="review__text">This is the second time we have used Ashfield home improvements , and the service is amazing! Martin came round several times as we kept changing our minds and he was so helpful and gave us good advice, and the guys who did the fitting were efficient and tidy . I've got to say the end result is amazing and I have recommended them to many friends .<br>Thanks Ashfield</p>
        <p class="metrics"><span>Reliablity : <b class="hl">9.38</b></span><span>Courtesy : <b class="hl">10</b></span><span>Tidiness : <b class="hl">9.84</b></span><span>Workmanship : <b class="hl">10</b></span></p>
        <div class="meta-row"><p class="meta meta--plain"><svg><use href="#icon-verified"/></svg>Verified <b class="hl">28th September 2021</b></p><p class="meta meta--plain"><svg><use href="#icon-pin"/></svg>Located in <b class="hl">Hollowford</b></p></div>
      </div>
    </article>
    <article class="review" style="height:110px;margin-top:7px">
      <div class="review__source"><span class="brand brand--lg"><i class="brand__mark"></i>Searchly</span><span class="rating rating--lg">★★★★★</span></div>
      <div class="review__body">
        <h3 class="review__title">Positive: Professionalism, Quality, Value</h3>
        <p class="review__text">The team did a good job of replacing a large feature window spanning two floors, as well as the others in my property. They're a professional group who were willing to work out solutions to any problem, especially compared to other companies. Prices are fair, and my new UPVC windows look great. Special thanks to Owen for being so accommodating and for the good communication throughout.</p>
        <p class="metrics"><span>Service : <b class="hl">Window installation</b></span></p>
        <p class="meta"><svg><use href="#icon-time"/></svg><span>11 months ago by <span class="hl">Dana Whitcombe</span></span></p>
      </div>
    </article>
    <article class="review" style="height:103px;margin-top:7px">
      <div class="review__source"><span class="brand brand--lg"><i class="brand__mark"></i>Listwell</span><span class="rating rating--lg">★★★★★</span></div>
      <div class="review__body">
        <h3 class="review__title">Brilliant all round professional, friendly service</h3>
        <p class="review__text">This home run friendly business was a real pleasure to deal with. From the professional, no pressure quote, nothing was too much trouble to ensure everything was as required for your needs with the quote and fitting. The workmanship and double glazing being fitted was brilliant and my home/outdoors was left tidy and clean leaving an outstanding impression for such an all round professional job. I would not hesitate to recommend this company, such a brilliant service from great hardworking people that care about their service</p>
        <p class="meta"><svg><use href="#icon-time"/></svg><span>13 Feb 2018 by <span class="hl">GreenKettle42</span></span></p>
      </div>
    </article>
    <article class="review" style="height:93px;margin-top:8px">
      <div class="review__source"><span class="brand brand--lg"><i class="brand__mark"></i>FairMark</span><span class="rating rating--lg">★★★★★</span></div>
      <div class="review__body">
        <h3 class="review__title">Front door with windows each side and side window</h3>
        <p class="review__text">This is the second time we have used Ashfield Home Improvements , and the service is amazing! Martin came round several times as we kept changing our minds and he was so helpful and gave us good advice, and the guys who did the fitting were efficient and tidy . I've got to say the end result is amazing and I have recommended them to many friends . Thanks Ashfield</p>
        <p class="meta"><svg><use href="#icon-time"/></svg><span>13 Feb 2018 by <span class="hl">Priya</span></span></p>
      </div>
    </article>
  </div>
  <footer class="footer">
    <button class="load-more">Load More</button>
    <div class="powered"><span class="powered__label">Powered by</span><span class="powered__name"><i></i>ReviewWeave</span></div>
  </footer>
</section>

<!-- Contained screen -->
<section class="widget widget--contained">
  <header class="score">
    <div class="score__stars"><svg><use href="#star-badge"/></svg><svg><use href="#star-badge"/></svg><svg><use href="#star-badge"/></svg><svg><use href="#star-badge"/></svg><svg><use href="#star-badge"/></svg></div>
    <p class="score__caption">Combined Review Score 4.3 out of 5</p>
  </header>
  <div class="reviews">
    <article class="review" style="height:115px">
      <div class="review__source"><span class="brand brand--lg"><i class="brand__mark"></i>TradeTally</span><div class="score-ring">9.77</div></div>
      <div class="review__body">
        <h3 class="review__title">Front door with windows each side and side window</h3>
        <p class="review__text">This is the second time we have used Ashfield home improvements , and the service is amazing! Martin came round several times as we kept changing our minds and he was so helpful and gave us good advice, and the guys who did the fitting were efficient and tidy . I've got to say the end result is amazing and I have recommended them to many friends . Thanks Ashfield</p>
        <p class="metrics"><span>Reliablity : <b class="hl">9.38</b></span><span>Courtesy : <b class="hl">10</b></span><span>Tidiness : <b class="hl">9.84</b></span><span>Workmanship : <b class="hl">10</b></span></p>
        <div class="meta-row"><p class="meta meta--plain"><svg><use href="#icon-verified"/></svg>Verified <b class="hl">28th September 2021</b></p><p class="meta meta--plain"><svg><use href="#icon-pin"/></svg>Located in <b class="hl">Hollowford</b></p></div>
      </div>
    </article>
    <article class="review" style="height:109px;margin-top:7px">
      <div class="review__source"><span class="brand brand--lg"><i class="brand__mark"></i>Searchly</span><span class="rating rating--lg">★★★★★</span></div>
      <div class="review__body">
        <h3 class="review__title">Positive: Professionalism, Quality, Value</h3>
        <p class="review__text">The team did a good job of replacing a large feature window spanning two floors, as well as the others in my property. They're a professional group who were willing to work out solutions to any problem, especially compared to other companies. Prices are fair, and my new UPVC windows look great. Special thanks to Owen for being so accommodating and for the good communication throughout.</p>
        <p class="metrics"><span>Service : <b class="hl">Window installation</b></span></p>
        <p class="meta"><svg><use href="#icon-time"/></svg><span>11 months ago by <span class="hl">Dana Whitcombe</span></span></p>
      </div>
    </article>
    <article class="review" style="height:105px;margin-top:9px">
      <div class="review__source"><span class="brand brand--lg"><i class="brand__mark"></i>Listwell</span><span class="rating rating--lg">★★★★★</span></div>
      <div class="review__body">
        <h3 class="review__title">Brilliant all round professional, friendly service</h3>
        <p class="review__text" style="margin-top:5px">This home run friendly business was a real pleasure to deal with. From the professional, no pressure quote, nothing was too much trouble to ensure everything was as required for your needs with the quote and fitting. The workmanship and double glazing being fitted was brilliant and my home/outdoors was left tidy and clean leaving an outstanding impression for such an all round professional job. I would not hesitate to recommend this company, such a brilliant service from great hardworking people that care about their service</p>
        <p class="meta"><svg><use href="#icon-time"/></svg><span>13 Feb 2018 by <span class="hl">GreenKettle42</span></span></p>
      </div>
    </article>
    <article class="review" style="height:97px;margin-top:8px">
      <div class="review__source"><span class="brand brand--lg"><i class="brand__mark"></i>FairMark</span><span class="rating rating--lg">★★★★★</span></div>
      <div class="review__body">
        <h3 class="review__title">Front door with windows each side and side window</h3>
        <p class="review__text" style="margin-top:5px">This is the second time we have used Ashfield Home Improvements , and the service is amazing! Martin came round several times as we kept changing our minds and he was so helpful and gave us good advice, and the guys who did the fitting were efficient and tidy . I've got to say the end result is amazing and I have recommended them to many friends . Thanks Ashfield</p>
        <p class="meta"><svg><use href="#icon-time"/></svg><span>13 Feb 2018 by <span class="hl">Priya</span></span></p>
      </div>
    </article>
  </div>
  <footer class="footer">
    <button class="load-more">Load More</button>
    <div class="powered"><span class="powered__label">Powered by</span><span class="powered__name"><i></i>ReviewWeave</span></div>
  </footer>
</section>

<!-- Mobile screen -->
<section class="widget widget--mobile">
  <header class="score">
    <div class="score__stars"><svg><use href="#star-badge"/></svg><svg><use href="#star-badge"/></svg><svg><use href="#star-badge"/></svg><svg><use href="#star-badge"/></svg><svg><use href="#star-badge"/></svg></div>
    <p class="score__caption">Combined Review Score 4.3 out of 5</p>
  </header>
  <div class="reviews">
    <article class="review" style="height:266px">
      <div class="review__source" style="height:70px;margin-top:2px"><span class="brand brand--md"><i class="brand__mark"></i>TradeTally</span><div class="score-ring score-ring--sm">9.77</div></div>
      <div class="review__body">
        <h3 class="review__title">Front door with windows each side and side window</h3>
        <p class="review__text">This is the second time we have used Ashfield home improvements , and the service is amazing! Martin came round several times as we kept changing our minds and he was so helpful and gave us good advice, and the guys who did the fitting were efficient and tidy . I've got to say the end result is amazing and I have recommended them to many friends . Thanks Ashfield</p>
        <p class="metrics"><span>Reliablity : <b class="hl">9.38</b></span><span>Courtesy : <b class="hl">10</b></span><span>Tidiness : <b class="hl">9.84</b></span><span style="padding-left:0;border-left:none">Workmanship : <b class="hl">10</b></span></p>
        <p class="meta meta--plain meta--big"><svg><use href="#icon-pin"/></svg>Located in <b class="hl">Hollowford</b></p>
        <p class="meta meta--plain meta--big" style="margin-top:9px"><svg><use href="#icon-verified"/></svg>Verified <b class="hl">28th September 2021</b></p>
      </div>
    </article>
    <article class="review" style="height:218px;margin-top:14px">
      <div class="review__source" style="height:70px"><span class="brand brand--md"><i class="brand__mark"></i>Searchly</span><span class="rating rating--md">★★★★★</span></div>
      <div class="review__body">
        <h3 class="review__title">Positive: Professionalism, Quality, Value</h3>
        <p class="review__text">The team did a good job of replacing a large feature window spanning two floors, as well as the others in my property. They're a professional group who were willing to work out solutions to any problem, especially compared to other companies. Prices are fair, and my new UPVC windows look great. Special thanks to Owen for being so accommodating and for the good communication throughout.</p>
        <p class="metrics"><span>Service : <b class="hl">Window installation</b></span></p>
        <p class="meta"><svg><use href="#icon-time"/></svg><span>11 months ago by <span class="hl">Dana Whitcombe</span></span></p>
      </div>
    </article>
    <article class="review" style="height:227px;margin-top:13px">
      <div class="review__source" style="height:70px"><span class="brand brand--md"><i class="brand__mark"></i>Listwell</span><span class="rating rating--md">★★★★★</span></div>
      <div class="review__body">
        <h3 class="review__title">Brilliant all round professional, friendly service</h3>
        <p class="review__text">This home run friendly business was a real pleasure to deal with. From the professional, no pressure quote, nothing was too much trouble to ensure everything is as required for your needs with the quote and fitting. The workmanship and double glazing being fitted was brilliant and my home/outdoors was left tidy and clean leaving an outstanding impression for such an all round professional job. I would not hesitate to recommend this company, such a brilliant service from great hardworking people that care about their service</p>
        <p class="meta"><svg><use href="#icon-time"/></svg><span>13 Feb 2018 by <span class="hl">GreenKettle42</span></span></p>
      </div>
    </article>
    <article class="review" style="height:209px;margin-top:17px">
      <div class="review__source" style="height:72px;flex-direction:column;gap:6px"><span class="brand brand--md"><i class="brand__mark"></i>FairMark</span><span class="rating rating--md">★★★★★</span></div>
      <div class="review__body">
        <h3 class="review__title">Front door with windows each side and side window</h3>
        <p class="review__text">This is the second time we have used Ashfield home Improvements , and the service is amazing! Martin came round several times as we kept changing our minds and he was so helpful and gave us good advice, and the guys who did the fitting were efficient and tidy . I've got to say the end result is amazing and I have recommended them to many friends . Thanks Ashfield</p>
        <p class="meta"><svg><use href="#icon-time"/></svg><span>13 Feb 2018 by <span class="hl">Priya</span></span></p>
      </div>
    </article>
  </div>
  <footer class="footer">
    <button class="load-more">Load More</button>
    <div class="powered"><span class="powered__label">Powered by</span><span class="powered__name"><i></i>ReviewWeave</span></div>
  </footer>
</section>
</body>
</html>
```